Need Business Cards, Letterhead, and Stationary

Hi, please design a full stationary set for the attached logo (Business Cards, Letterhead, A4 Envelope, and other important stationary items that you can think of)
Please be as creative as you wish. The logo is for An Entrepreneurship Academy that teaches young and starting Entrepreneur skills they need to start their business.
Business
Serif
Sans Serif

```html
<!DOCTYPE html>
<html lang="en">
<head>
<meta charset="utf-8">
<title>Sprout Founders Academy – Stationery</title>
<link rel="stylesheet" href="https://fonts.googleapis.com/css2?family=Ubuntu:wght@400;500;700&display=swap">
<style>
  :root {
    --backdrop: #dedede;
    --sheet-dark: #100f0f;
    --sheet-light: #ffffff;
    --ink: #2b2b2b;
    --ink-muted: #6f6f6f;
    --brand-yellow: #f5c800;
    --brand-grey: #7b7b7d;
    --brand-blue: #0f6fb6;
    --brand-black: #242424;
    --brand-white: #ffffff;
  }
  * { margin: 0; padding: 0; box-sizing: border-box; }
  html, body { width: 1200px; height: 900px; overflow: hidden; }
  body {
    position: relative;
    background: var(--backdrop);
    font-family: "Ubuntu", Arial, sans-serif;
    color: var(--ink);
  }
  .sheet {
    position: absolute;
    top: 93px;
    width: 503px;
    height: 712px;
    box-shadow: 0 6px 14px rgba(0,0,0,0.18);
  }
  .folder-cover {
    left: 74px;
    background: var(--sheet-dark);
    display: flex;
    align-items: center;
    justify-content: center;
  }
  .cover-brand {
    display: flex;
    align-items: center;
    gap: 12px;
    color: var(--brand-white);
    font-weight: 700;
    font-size: 26px;
    letter-spacing: 2px;
    text-transform: uppercase;
  }
  .brand-dot {
    width: 20px; height: 20px;
    border-radius: 50%;
    background: var(--brand-yellow);
    flex: none;
  }
  .letterhead {
    left: 608px;
    background: var(--sheet-light);
  }
  .letterhead-brand {
    position: absolute;
    left: 26px; top: 42px;
    display: flex;
    align-items: center;
    gap: 8px;
    color: var(--ink);
    font-weight: 700;
    font-size: 17px;
    letter-spacing: 0.5px;
  }
  .letterhead-brand .brand-dot { width: 14px; height: 14px; }
  .sender {
    position: absolute;
    left: 23px; top: 650px;
    font-size: 8px;
    line-height: 10px;
    color: var(--ink);
  }
  .sender-name { font-size: 6px; color: var(--ink-muted); margin-bottom: 3px; }
  .sender-contacts { display: flex; gap: 8px; margin-top: 4px; }
  .contact { display: flex; align-items: center; gap: 3px; }
  .contact svg { width: 10px; height: 10px; }
  .website {
    position: absolute;
    right: 41px; top: 684px;
    font-size: 8px;
    font-weight: 700;
    color: var(--ink);
  }
  .colour-strip {
    position: absolute;
    right: 0; bottom: 0;
    display: flex;
    height: 8px;
  }
  .colour-strip span { width: 37px; height: 100%; }
  .strip-yellow { background: var(--brand-yellow); }
  .strip-grey { background: var(--brand-grey); }
  .strip-blue { background: var(--brand-blue); }
  .strip-black { background: var(--brand-black); }
</style>
</head>
<body>
  <section class="sheet folder-cover">
    <div class="cover-brand"><span class="brand-dot"></span>Sprout</div>
  </section>

  <section class="sheet letterhead">
    <div class="letterhead-brand"><span class="brand-dot"></span>Sprout Founders Academy</div>

    <address class="sender" style="font-style: normal;">
      <div class="sender-name">Sprout Founders Academy</div>
      <div>Office Building Street</div>
      <div>City, 00000 Country</div>
      <div class="sender-contacts">
        <span class="contact">
          <svg viewBox="0 0 10 10" aria-hidden="true"><rect x="2" y="0.5" width="6" height="9" rx="1" fill="none" stroke="#2b2b2b" stroke-width="1"/><line x1="4" y1="8" x2="6" y2="8" stroke="#2b2b2b"/></svg>
          000 0000 0000
        </span>
        <span class="contact">
          <svg viewBox="0 0 10 10" aria-hidden="true"><rect x="1" y="4" width="8" height="5" fill="none" stroke="#2b2b2b" stroke-width="1"/><rect x="3" y="1" width="4" height="3" fill="none" stroke="#2b2b2b" stroke-width="1"/></svg>
          000 0000 0000
        </span>
      </div>
    </address>

    <div class="website">www.sproutfa.com</div>

    <div class="colour-strip">
      <span class="strip-yellow"></span>
      <span class="strip-grey"></span>
      <span class="strip-blue"></span>
      <span class="strip-black"></span>
    </div>
  </section>
</body>
</html>
```